" Empresa atua como intermediadora de negócios, facilitadora de soluções relacionadas à regularização de imóveis, gestão de propriedade imobiliária, compra, venda e locação, consultoria de investimentos. "

```html
<!DOCTYPE html>
<html lang="pt-BR">
<head>
<meta charset="UTF-8">
<title>Valorim Assessoria Imobiliária – Cartão de visita</title>
<link rel="stylesheet" href="https://fonts.googleapis.com/css2?family=Montserrat:wght@400;500;600&display=swap">
<style>
  :root {
    --page-bg: #e9e9e7;
    --card-dark: #1b1b1b;
    --card-light: #ffffff;
    --ink-dark: #3a3a3a;
    --ink-light: #e6e6e6;
    --gold: #b08d4f;
    --gold-soft: #c9a96a;
    --muted: #6b6b6b;
  }
  * { box-sizing: border-box; margin: 0; padding: 0; }
  html, body {
    width: 1200px; height: 1200px; overflow: hidden;
    background: var(--page-bg);
    font-family: "Montserrat", Arial, sans-serif;
  }
  .sheet {
    width: 1200px; height: 1200px;
    display: flex; flex-direction: column;
    align-items: center; justify-content: center; gap: 60px;
  }
  .card {
    width: 900px; height: 500px;
    border-radius: 36px;
    position: relative;
    box-shadow: 0 10px 30px rgba(0,0,0,0.12);
    overflow: hidden;
  }
  .card--back {
    background: var(--card-dark);
    display: flex; align-items: center; justify-content: center;
  }
  .card--front { background: var(--card-light); }

  .brand { display: flex; flex-direction: column; }
  .brand__name {
    font-weight: 500;
    letter-spacing: 0.08em;
    line-height: 1;
  }
  .brand__tagline {
    color: var(--gold);
    font-weight: 400;
    text-transform: uppercase;
    letter-spacing: 0.12em;
  }
  .card--back .brand { align-items: flex-start; margin-left: 120px; }
  .card--back .brand__name { color: var(--ink-light); font-size: 96px; }
  .card--back .brand__tagline { font-size: 27px; margin-top: 10px; }

  .card--front .brand { position: absolute; left: 120px; top: 70px; }
  .card--front .brand__name { color: var(--ink-dark); font-size: 64px; }
  .card--front .brand__tagline { font-size: 18px; margin-top: 8px; letter-spacing: 0.16em; }

  .contacts {
    position: absolute; left: 120px; top: 215px;
    list-style: none;
    display: flex; flex-direction: column; gap: 12px;
    color: var(--muted); font-size: 19px;
  }
  .contacts li { display: flex; align-items: flex-start; gap: 14px; line-height: 1.3; }
  .contacts svg { flex: none; width: 26px; height: 26px; margin-top: -1px; }
  .contacts .address { display: flex; flex-direction: column; }
</style>
</head>
<body>
<main class="sheet">
  <section class="card card--back">
    <div class="brand">
      <span class="brand__name">VALORIM</span>
      <span class="brand__tagline">Assessoria Imobiliária</span>
    </div>
  </section>

  <section class="card card--front">
    <div class="brand">
      <span class="brand__name">VALORIM</span>
      <span class="brand__tagline">Assessoria Imobiliária</span>
    </div>
    <ul class="contacts">
      <li>
        <svg viewBox="0 0 26 26" aria-hidden="true"><circle cx="13" cy="13" r="12" fill="var(--gold-soft)"/><path d="M9 7.5l2.2 0.3 1 3-1.4 1.2a7 7 0 0 0 3.2 3.2l1.2-1.4 3 1 .3 2.2c-.8.8-1.8 1.2-3 1-4-.7-7.3-4-8-8-.2-1.2.2-2.2 1-3z" fill="#fff"/></svg>
        <span>011 900004321</span>
      </li>
      <li>
        <svg viewBox="0 0 26 26" aria-hidden="true"><circle cx="13" cy="13" r="12" fill="var(--gold-soft)"/><rect x="7" y="9" width="12" height="8.5" rx="1" fill="none" stroke="#fff" stroke-width="1.5"/><path d="M7.5 9.5l5.5 4.5 5.5-4.5" fill="none" stroke="#fff" stroke-width="1.5"/></svg>
        <span>contato@valorim.com.br</span>
      </li>
      <li>
        <svg viewBox="0 0 26 26" aria-hidden="true"><circle cx="13" cy="13" r="12" fill="var(--gold-soft)"/><circle cx="13" cy="13" r="6" fill="none" stroke="#fff" stroke-width="1.4"/><ellipse cx="13" cy="13" rx="2.6" ry="6" fill="none" stroke="#fff" stroke-width="1.2"/><path d="M7 13h12" stroke="#fff" stroke-width="1.2"/></svg>
        <span>www.valorim.com.br</span>
      </li>
      <li>
        <svg viewBox="0 0 26 26" aria-hidden="true"><circle cx="13" cy="13" r="12" fill="var(--gold-soft)"/><path d="M13 6.5a4.5 4.5 0 0 0-4.5 4.5c0 3.3 4.5 8.5 4.5 8.5s4.5-5.2 4.5-8.5A4.5 4.5 0 0 0 13 6.5z" fill="#fff"/><circle cx="13" cy="11" r="1.6" fill="var(--gold-soft)"/></svg>
        <span class="address"><span>Rua das Acácias, 120 - sala 204</span><span>Campinas/SP</span></span>
      </li>
    </ul>
  </section>
</main>
</body>
</html>
```